Business Card Design for Engineering Firm

Need a business card design for small mechanical and plumbing engineering form based in Utah. Design should be customizable for all employees.

```html
<!DOCTYPE html>
<html lang="en">
<head>
<meta charset="utf-8">
<title>Ridgeline Engineering – Business Card</title>
<link href="https://fonts.googleapis.com/css2?family=Montserrat:wght@500;600;700&family=Lato:wght@400;700&display=swap" rel="stylesheet">
<style>
  :root {
    --backdrop: #2b2c2e;
    --backdrop-light: #3a3b3d;
    --card-dark: #3e3e40;
    --card-light: #ffffff;
    --brand-red: #8c1214;
    --ink: #3a3a3a;
    --ink-soft: #666666;
    --rule: #bdbdbd;
  }
  * { box-sizing: border-box; margin: 0; padding: 0; }
  html, body { width: 1200px; height: 952px; overflow: hidden; }
  body {
    background: radial-gradient(ellipse at 60% 35%, var(--backdrop-light), var(--backdrop) 75%);
    display: flex;
    align-items: center;
    justify-content: center;
    gap: 50px;
    font-family: "Lato", sans-serif;
  }
  .card {
    width: 525px;
    height: 300px;
    border-radius: 22px;
    position: relative;
    box-shadow: 0 14px 30px rgba(0,0,0,0.45);
  }
  /* Front */
  .card-front {
    background: var(--card-dark);
    display: flex;
    align-items: center;
    justify-content: center;
    gap: 18px;
  }
  .brand-mark {
    width: 40px;
    height: 40px;
    border: 3px solid #ffffff;
  }
  .brand-name {
    font-family: "Montserrat", sans-serif;
    font-weight: 600;
    color: #ffffff;
    font-size: 26px;
    letter-spacing: 1px;
    line-height: 1.1;
  }
  .brand-name .sub {
    display: block;
    font-size: 12px;
    letter-spacing: 9px;
    margin-top: 6px;
  }
  /* Back */
  .card-back { background: var(--card-light); overflow: hidden; }
  .back-brand {
    position: absolute;
    top: 36px;
    left: 40px;
    display: flex;
    align-items: center;
    gap: 14px;
  }
  .back-brand .brand-mark {
    width: 30px;
    height: 30px;
    border-color: var(--brand-red);
  }
  .back-brand .divider {
    width: 1px;
    height: 40px;
    background: var(--rule);
  }
  .back-brand .brand-name {
    color: var(--brand-red);
    font-size: 17px;
  }
  .back-brand .brand-name .sub {
    font-size: 8px;
    letter-spacing: 5px;
    margin-top: 3px;
  }
  .contact-list {
    position: absolute;
    left: 40px;
    top: 130px;
    list-style: none;
    font-size: 11px;
    color: var(--ink);
    line-height: 1.35;
  }
  .contact-list li {
    display: flex;
    align-items: flex-start;
    gap: 9px;
    margin-bottom: 9px;
  }
  .contact-icon {
    width: 14px;
    height: 14px;
    flex: none;
    background: var(--brand-red);
    border-radius: 2px;
    display: flex;
    align-items: center;
    justify-content: center;
  }
  .contact-icon.address { background: var(--ink); }
  .person {
    position: absolute;
    right: 42px;
    top: 150px;
    text-align: right;
  }
  .person-name {
    font-family: "Montserrat", sans-serif;
    color: var(--brand-red);
    font-size: 19px;
    font-weight: 500;
    letter-spacing: 0.5px;
  }
  .person-name strong { font-weight: 700; }
  .person-title {
    font-size: 13px;
    color: var(--ink-soft);
    margin-top: 4px;
    letter-spacing: 0.5px;
  }
  .person-rule {
    width: 70px;
    height: 1px;
    background: var(--ink);
    margin: 6px 0 0 auto;
  }
</style>
</head>
<body>

<section class="card card-front">
  <span class="brand-mark"></span>
  <div class="brand-name">RIDGELINE<span class="sub">ENGINEERING</span></div>
</section>

<section class="card card-back">
  <div class="back-brand">
    <span class="brand-mark"></span>
    <span class="divider"></span>
    <div class="brand-name">RIDGELINE<span class="sub">ENGINEERING</span></div>
  </div>

  <ul class="contact-list">
    <li>
      <span class="contact-icon address">
        <svg width="9" height="10" viewBox="0 0 9 10"><path d="M4.5 0.5a3.2 3.2 0 0 0-3.2 3.2c0 2.3 3.2 5.8 3.2 5.8s3.2-3.5 3.2-5.8A3.2 3.2 0 0 0 4.5 0.5z" fill="#fff"/><circle cx="4.5" cy="3.7" r="1.1" fill="#3a3a3a"/></svg>
      </span>
      <span>1250 Canyon Ridge Drive<br>Provo, UT 84604</span>
    </li>
    <li>
      <span class="contact-icon">
        <svg width="9" height="9" viewBox="0 0 9 9"><path d="M2 0.5l1.5 2-1 1c0.6 1.3 1.7 2.4 3 3l1-1 2 1.5-1 1.5C4 8.5 0.5 5 0.5 1.5z" fill="#fff"/></svg>
      </span>
      <span>+00 987 654 32</span>
    </li>
    <li>
      <span class="contact-icon">
        <svg width="10" height="8" viewBox="0 0 10 8"><rect x="0.5" y="0.5" width="9" height="7" fill="none" stroke="#fff"/><path d="M0.5 0.5l4.5 4 4.5-4" fill="none" stroke="#fff"/></svg>
      </span>
      <span>office@ridgelineeng.com</span>
    </li>
    <li>
      <span class="contact-icon">
        <svg width="10" height="10" viewBox="0 0 10 10"><circle cx="5" cy="5" r="4" fill="none" stroke="#fff"/><path d="M1 5h8M5 1c-2 2.5-2 5.5 0 8M5 1c2 2.5 2 5.5 0 8" fill="none" stroke="#fff" stroke-width="0.8"/></svg>
      </span>
      <span>www.ridgelineeng.com</span>
    </li>
  </ul>

  <div class="person">
    <div class="person-name">DANIEL M. <strong>HARTWELL</strong></div>
    <div class="person-title">Managing Director</div>
    <div class="person-rule"></div>
  </div>
</section>

</body>
</html>
```